Business Card and Letterhead for Pemlo - modern real estate business

I need a double sided business card design for Pemlo. Please see business card brief here https://files.quillnote-hub.net/page/7RtxQmZbn4LsWe2VyHoPk9dFjuC3gaXrTmqEi5Ns_pz/view?mode=shared

Please feel free to design the business cards however you feel best. I am happy to give some creative freedoms and then provide feedback from there.

Please then also create a letterhead to match the business card design

Colors

Designer to choose colors to be used in the design.

Requirements
Must have
• Must be a modern, elegant business card which looks very professional

```html
<!DOCTYPE html>
<html lang="en">
<head>
<meta charset="utf-8">
<title>Pemlo Business Card</title>
<link href="https://fonts.googleapis.com/css2?family=Michroma&family=Roboto:wght@400;500&display=swap" rel="stylesheet">
<style>
  :root {
    --stage: #1f1f1f;
    --red: #e31e24;
    --black: #141414;
    --white: #f8f8f8;
    --ink: #1a1a1a;
    --photo-top: #eef0f2;
    --photo-bottom: #3a3d42;
  }
  * { margin: 0; padding: 0; box-sizing: border-box; }
  html, body {
    width: 1200px; height: 865px; overflow: hidden;
    background: var(--stage);
  }
  .stage { position: relative; width: 1200px; height: 865px; }
  .card {
    position: absolute; left: 300px;
    width: 600px; height: 343px;
    border-radius: 18px; overflow: hidden;
  }
  .card--back { top: 52px; background: var(--black); }
  .card--front { top: 470px; background: var(--white); }

  .brand {
    font-family: "Michroma", sans-serif;
    color: var(--red);
    text-transform: uppercase;
    letter-spacing: 4px;
    line-height: 1;
  }
  .card--back .brand {
    position: absolute; left: 0; right: 0; top: 50%;
    transform: translateY(-50%);
    text-align: center; font-size: 82px;
  }
  .card--front .brand {
    position: absolute; left: 48px; top: 48px; font-size: 62px;
  }

  .photo {
    position: absolute; left: 372px; top: 26px;
    width: 200px; height: 230px;
    background: linear-gradient(180deg, var(--photo-top) 0%, var(--photo-bottom) 70%);
    border-radius: 100px 100px 0 0;
  }
  .wave { position: absolute; inset: 0; width: 600px; height: 343px; }

  .identity {
    position: absolute; left: 48px; top: 148px;
    padding-left: 14px; border-left: 8px solid var(--red);
  }
  .identity__name {
    font-family: "Michroma", sans-serif; font-size: 22px;
    color: var(--red); letter-spacing: 2px; text-transform: uppercase;
  }
  .identity__role {
    font-family: "Roboto", sans-serif; font-size: 15px; font-weight: 500;
    color: var(--ink); margin-top: 4px;
  }

  .contact {
    position: absolute; left: 58px; top: 246px;
    font-family: "Roboto", sans-serif; font-size: 13.5px;
    color: #fff; line-height: 17px; list-style: none;
  }
  .contact li { display: flex; align-items: center; gap: 7px; }
  .contact .icon { width: 12px; height: 12px; fill: #fff; }
  .contact .address { padding-left: 0; }

  .licence {
    position: absolute; right: 34px; top: 226px;
    font-family: "Roboto", sans-serif; font-size: 14px; font-weight: 500;
    color: #fff;
  }
</style>
</head>
<body>
<main class="stage">

  <section class="card card--back" aria-label="Card back">
    <div class="brand">Pemlo</div>
  </section>

  <section class="card card--front" aria-label="Card front">
    <div class="brand">Pemlo</div>

    <div class="photo" role="img" aria-label="Portrait photo of the agent in a dark suit"></div>

    <svg class="wave" viewBox="0 0 600 343" aria-hidden="true">
      <path fill="var(--black)" d="M0,343 L0,296 C80,200 250,180 380,176 C480,172 560,120 600,78 L600,343 Z"/>
      <path fill="var(--red)" d="M0,343 L0,318 C90,216 250,194 385,190 C490,186 570,136 600,100 L600,343 Z"/>
    </svg>

    <div class="identity">
      <div class="identity__name">Jordan Hale</div>
      <div class="identity__role">Real Estate Agent</div>
    </div>

    <ul class="contact">
      <li class="address">PO Box 3190</li>
      <li class="address">Larkfield NSW 2790</li>
      <li>
        <svg class="icon" viewBox="0 0 24 24"><path d="M6.6 10.8a15.1 15.1 0 0 0 6.6 6.6l2.2-2.2a1 1 0 0 1 1-.25 11.4 11.4 0 0 0 3.6.57 1 1 0 0 1 1 1V20a1 1 0 0 1-1 1A17 17 0 0 1 3 4a1 1 0 0 1 1-1h3.5a1 1 0 0 1 1 1c0 1.25.2 2.45.57 3.57a1 1 0 0 1-.25 1z"/></svg>
        0412 555 019
      </li>
      <li>
        <svg class="icon" viewBox="0 0 24 24"><path d="M2 5h20v14H2z M2 5l10 8 10-8" fill="#fff" stroke="var(--red)" stroke-width="1.5"/></svg>
        jordan@pemlo.com
      </li>
      <li>
        <svg class="icon" viewBox="0 0 24 24"><circle cx="12" cy="12" r="10"/><path d="M2 12h20M12 2c3 3 3 17 0 20M12 2c-3 3-3 17 0 20" fill="none" stroke="var(--red)" stroke-width="1.5"/></svg>
        www.pemlo.com
      </li>
    </ul>

    <div class="licence">Lic No. 10482391</div>
  </section>

</main>
</body>
</html>
```